Business Card Design

Business Card for professional consulting firm working with large financial institutions.

Target Market(s)

Executive buyers

Industry/Entity Type

Banking

Contact Information for Business Card

Mild creativity wanted. Not boring, but do elaborate artwork.

Font styles to use
Serif
Sans Serif

Colors

Designer to choose colors to be used in the design.

Requirements
Must have
• Standard business card features - company name, individual name, telephone, website, email, locations.
Nice to have
• Two colors
Should not have
• too many colors, fancy printing, cartoons.

```html
<!DOCTYPE html>
<html lang="en">
<head>
<meta charset="utf-8">
<title>Northvale Business Card</title>
<link href="https://fonts.googleapis.com/css2?family=EB+Garamond:wght@400;500;600&display=swap" rel="stylesheet">
<style>
  :root {
    --backdrop: #3a3a3c;
    --card-dark: #161616;
    --card-light: #ffffff;
    --ink: #151515;
    --ink-soft: #333333;
    --on-dark: #f2f2f2;
    --accent-gold: #b39a66;
    --mark-grey: #bdbdbd;
  }
  * { box-sizing: border-box; margin: 0; padding: 0; }
  html, body {
    width: 1200px; height: 1000px; overflow: hidden;
    background: var(--backdrop);
    font-family: "EB Garamond", Georgia, serif;
  }
  .stage { position: relative; width: 1200px; height: 1000px; }
  .card {
    position: absolute; left: 250px; width: 700px; height: 400px;
    border-radius: 26px; overflow: hidden;
  }
  .card--back { top: 70px; background: var(--card-dark); }
  .card--front { top: 530px; background: var(--card-light); }

  .brand { position: absolute; display: flex; align-items: center; gap: 14px; }
  .brand__dot { width: 14px; height: 14px; border-radius: 50%; }
  .brand__name { font-weight: 400; letter-spacing: 1px; line-height: 1; }

  .card--back .brand { left: 50%; top: 50%; transform: translate(-50%, -50%); }
  .card--back .brand__dot { background: var(--on-dark); }
  .card--back .brand__name { color: var(--on-dark); font-size: 66px; }

  .card--front .brand { left: 370px; top: 78px; }
  .card--front .brand__dot { background: var(--mark-grey); }
  .card--front .brand__name { color: var(--ink); font-size: 54px; }

  .person { position: absolute; left: 150px; top: 200px; text-align: right; width: 190px; }
  .person__name { font-size: 23px; letter-spacing: 1px; color: var(--ink-soft); text-transform: uppercase; }
  .person__title { font-size: 12px; font-weight: 600; letter-spacing: 1px; color: var(--ink); text-transform: uppercase; margin-top: 2px; }

  .contact { position: absolute; left: 385px; top: 228px; color: var(--ink); font-size: 16px; font-weight: 500; }
  .contact__row { display: flex; align-items: flex-start; gap: 10px; margin-bottom: 4px; }
  .contact__row--address { margin-bottom: 20px; line-height: 1.3; }
  .contact__icon { width: 14px; height: 14px; flex: none; margin-top: 3px; fill: var(--accent-gold); }
</style>
</head>
<body>
<main class="stage">
  <section class="card card--back" aria-label="Card back">
    <div class="brand">
      <span class="brand__dot"></span>
      <span class="brand__name">northvale</span>
    </div>
  </section>

  <section class="card card--front" aria-label="Card front">
    <div class="brand">
      <span class="brand__dot"></span>
      <span class="brand__name">northvale</span>
    </div>

    <div class="person">
      <p class="person__name">Daniel Hart</p>
      <p class="person__title">General Manager</p>
    </div>

    <div class="contact">
      <div class="contact__row contact__row--address">
        <svg class="contact__icon" viewBox="0 0 24 24"><path d="M12 2a7 7 0 0 0-7 7c0 5 7 13 7 13s7-8 7-13a7 7 0 0 0-7-7zm0 9.5A2.5 2.5 0 1 1 12 6.5a2.5 2.5 0 0 1 0 5z"/></svg>
        <span>40 W Meridian Street Harbor Point Tower<br>12th Floor Tempe, Arizona 85281</span>
      </div>
      <div class="contact__row">
        <svg class="contact__icon" viewBox="0 0 24 24"><path d="M6.6 10.8a15 15 0 0 0 6.6 6.6l2.2-2.2a1 1 0 0 1 1-.25 11.4 11.4 0 0 0 3.6.57 1 1 0 0 1 1 1V20a1 1 0 0 1-1 1A17 17 0 0 1 3 4a1 1 0 0 1 1-1h3.5a1 1 0 0 1 1 1c0 1.25.2 2.45.57 3.6a1 1 0 0 1-.25 1z"/></svg>
        <span>+602-555-0147</span>
      </div>
      <div class="contact__row">
        <svg class="contact__icon" viewBox="0 0 24 24"><path d="M3 5h18v14H3zm2 2v.5l7 4.5 7-4.5V7zm0 2.9V17h14V9.9l-7 4.5z"/></svg>
        <span>hello@northvale.us</span>
      </div>
      <div class="contact__row">
        <svg class="contact__icon" viewBox="0 0 24 24"><path d="M12 2a10 10 0 1 0 0 20 10 10 0 0 0 0-20zm6.9 6h-3a15 15 0 0 0-1.3-3.6A8 8 0 0 1 18.9 8zM12 4c.8 1.2 1.5 2.5 1.9 4h-3.8c.4-1.5 1.1-2.8 1.9-4zM4.3 14a8 8 0 0 1 0-4h3.4a16 16 0 0 0 0 4zm.8 2h3a15 15 0 0 0 1.3 3.6A8 8 0 0 1 5.1 16zm3-8h-3a8 8 0 0 1 4.3-3.6A15 15 0 0 0 8.1 8zM12 20c-.8-1.2-1.5-2.5-1.9-4h3.8c-.4 1.5-1.1 2.8-1.9 4zm2.3-6H9.7a14 14 0 0 1 0-4h4.6a14 14 0 0 1 0 4zm.3 5.6a15 15 0 0 0 1.3-3.6h3a8 8 0 0 1-4.3 3.6zm1.7-5.6a16 16 0 0 0 0-4h3.4a8 8 0 0 1 0 4z"/></svg>
        <span>www.northvale.us</span>
      </div>
    </div>
  </section>
</main>
</body>
</html>
```